Zanquorra Business Card Design

Zanquorra is a small and new restaurant/ bar location in Hong Kong. The name "Djibouti" derives from an African country. There is no specific reason behind other than the fact, that the bar is somewhat inspired by African elements (only inspired but not purely based on African cuisine etc.).

The bar is somewhat a fusion of African, Mediterranean and Oriental (Old French Vietnam) elements.

However, it is very imperative to stress, that the overall look and feel of Zanquorra is a very high end cocktail lounge/ bar location. The bar is tucked away in a hidden alley, so people will have to know about it. The idea is to send the consumer off in an Escape or hidden remote location where they are at ease in a hip, stylish and trendy environment.

The card needs to feel high-end.

Final logo artwork has been attached and also pictures of the bar/ restaurant itself. The logo ie monkey head cannot be modified. However, the background color and the color of the type "ZANQUORRA" can be changed.

The following details need to fit onto the business card. Of course they can be arranged to your liking:

LOGO

Colin Vey
Partner

+852 97035164
xxx@zanquorra.com
www.zanquorra.com
7C, Brennick Road, Wan Chai, Hong Kong

```html
<!DOCTYPE html>
<html lang="en">
<head>
<meta charset="utf-8">
<title>Zanquorra Business Card</title>
<link rel="stylesheet" href="https://fonts.googleapis.com/css2?family=Arimo:wght@400;700&display=swap">
<style>
  :root {
    --page: #ecebe8;
    --card-dark: #2e1f1c;
    --card-light: #f6f6f6;
    --ink: #141414;
    --name-blue: #1f4fa3;
    --role-red: #d2231e;
    --wordmark-dark: #222222;
    --wordmark-light: #f4e9ec;
    --mark-dark: #4a3a33;
    --mark-glow: #e2507f;
    --photo-deep: #1b1513;
    --photo-mid: #5a5654;
    --photo-light: #cfcfcf;
  }
  * { box-sizing: border-box; margin: 0; padding: 0; }
  html, body { width: 1200px; height: 900px; overflow: hidden; }
  body {
    background: var(--page);
    font-family: "Arimo", Arial, sans-serif;
    position: relative;
  }
  .card {
    position: absolute;
    left: 290px;
    width: 620px;
    height: 354px;
    box-shadow: 0 6px 18px rgba(0,0,0,0.18);
    overflow: hidden;
  }
  .card--back {
    top: 70px;
    background: var(--card-dark);
    display: flex;
    flex-direction: column;
    align-items: center;
    justify-content: center;
    gap: 14px;
  }
  .card--front {
    top: 476px;
    background: var(--card-light);
  }
  .brand-mark {
    width: 84px;
    height: 84px;
    border-radius: 50%;
    background: var(--mark-dark);
    border: 3px solid var(--mark-glow);
  }
  .brand-name {
    font-family: "Arimo", Arial, sans-serif;
    font-weight: 700;
    letter-spacing: 2px;
  }
  .card--back .brand-name {
    color: var(--wordmark-light);
    font-size: 28px;
  }
  .front-identity {
    position: absolute;
    left: 72px;
    top: 28px;
    display: flex;
    flex-direction: column;
    align-items: center;
    gap: 8px;
  }
  .front-identity .brand-mark {
    width: 70px;
    height: 70px;
    border: none;
    background: var(--mark-dark);
  }
  .card--front .brand-name {
    color: var(--wordmark-dark);
    font-size: 22px;
  }
  .person {
    position: absolute;
    left: 72px;
    top: 150px;
  }
  .person-name {
    color: var(--name-blue);
    font-weight: 700;
    font-size: 22px;
    letter-spacing: 0.5px;
  }
  .person-role {
    color: var(--role-red);
    font-size: 13px;
    margin-top: 1px;
  }
  .contact {
    position: absolute;
    left: 52px;
    top: 214px;
    font-size: 14px;
    line-height: 18px;
    color: var(--ink);
    list-style: none;
  }
  .alley-photo {
    position: absolute;
    right: 0;
    top: 0;
    width: 292px;
    height: 100%;
    background: linear-gradient(135deg, var(--photo-deep) 0%, var(--photo-mid) 55%, var(--photo-light) 100%);
  }
</style>
</head>
<body>
  <section class="card card--back">
    <div class="brand-mark"></div>
    <div class="brand-name">ZANQUORRA</div>
  </section>

  <section class="card card--front">
    <div class="front-identity">
      <div class="brand-mark"></div>
      <div class="brand-name">ZANQUORRA</div>
    </div>
    <div class="person">
      <div class="person-name">TAVIN ROE</div>
      <div class="person-role">manager</div>
    </div>
    <ul class="contact">
      <li>Suite 208 Harlow tower</li>
      <li>Merrow square MSQ-3, Eastvale, Norland</li>
      <li>Phone: 976-70458213 , Fax: 976- 70458290</li>
      <li>e-mail: enquiry@velmora.com</li>
    </ul>
    <div class="alley-photo" role="img" aria-label="Black and white photograph of the narrow hidden alley leading to the bar"></div>
  </section>
</body>
</html>
```